Bytemill - a software development company requires letter head

I currently have a business card and logo, I just need a nice looking letter head the matches the two. I will upload these Illustrator files.

I would like the letter head to be done in a current version of MS Word.

Please incorporate 'bytemill' as per the attached font and the logo.

Industry/Entity Type

Computer Software

Colors

Designer to choose colors to be used in the design.

Requirements
Must have
• Fits in with current design, sleek and professional. It will be used for quotations and tenders and documentation going to clients and potential clients.
• Would like to company logo up the top header and perhaps a watermark of the logo at the bottom right, a bit like the business card.
• Also it needs to be MS word.
• Please work with the color pallet from the attached files.

```html
<!DOCTYPE html>
<html lang="en">
<head>
<meta charset="utf-8">
<title>Bytemill Letterhead</title>
<link href="https://fonts.googleapis.com/css2?family=Open+Sans:wght@400;600;700&display=swap" rel="stylesheet">
<style>
  :root {
    --backdrop: #8a8580;
    --paper: #ffffff;
    --ink: #3a3a3a;
    --ink-soft: #6b6b6b;
    --brand-blue: #1f9ad6;
    --brand-dark: #3b3b3d;
    --watermark: #e6f1fa;
  }
  * { margin: 0; padding: 0; box-sizing: border-box; }
  html, body { width: 1200px; height: 795px; overflow: hidden; }
  body {
    background: var(--backdrop);
    font-family: "Open Sans", Arial, sans-serif;
    color: var(--ink);
    position: relative;
  }
  .letterhead {
    position: absolute;
    left: 331px; top: 17px;
    width: 537px; height: 760px;
    background: var(--paper);
    overflow: hidden;
  }
  .brand {
    position: absolute; left: 40px; top: 92px;
    display: flex; align-items: center; gap: 10px;
  }
  .brand-dot {
    width: 30px; height: 30px; border-radius: 50%;
    background: var(--brand-blue);
  }
  .brand-name {
    font-size: 24px; font-weight: 600; letter-spacing: 1px;
    color: var(--brand-dark); text-transform: uppercase;
  }
  .contact {
    position: absolute; left: 300px; top: 64px;
    font-size: 7.5px; line-height: 10px; color: var(--ink-soft);
  }
  .contact-title { color: var(--brand-blue); font-weight: 600; text-transform: uppercase; }
  .contact-row { display: flex; align-items: center; gap: 4px; }
  .contact-icon { width: 7px; height: 7px; }
  .letter {
    position: absolute; left: 60px; top: 168px; width: 380px;
    font-size: 8.5px; line-height: 11.5px;
  }
  .date { margin-bottom: 8px; }
  .recipient { margin-bottom: 10px; }
  .salutation { font-weight: 700; margin-bottom: 14px; }
  .letter p { color: var(--ink-soft); margin-bottom: 12px; }
  .closing { margin-top: 18px; }
  .signature {
    width: 70px; height: 20px; margin: 6px 0 4px 18px;
    background: linear-gradient(90deg, #e4e4e4, #f3f3f3);
  }
  .watermark {
    position: absolute; left: 400px; top: 540px;
    width: 170px; height: 170px; border-radius: 50%;
    background: var(--watermark);
  }
  .side-bar {
    position: absolute; right: 0; top: 420px; bottom: 30px; width: 22px;
    background: var(--brand-dark);
    display: flex; align-items: center; justify-content: center;
  }
  .side-bar span {
    transform: rotate(90deg); white-space: nowrap;
    color: #ffffff; font-size: 8px; letter-spacing: 2px;
  }
  .footer-bands { position: absolute; left: 0; bottom: 0; width: 537px; height: 90px; }
</style>
</head>
<body>
  <main class="letterhead">
    <div class="brand">
      <div class="brand-dot"></div>
      <div class="brand-name">Bytemill</div>
    </div>

    <address class="contact">
      <div class="contact-title">Bytemill</div>
      <div>PO Box 218, Northgate SA 5085</div>
      <div class="contact-row">
        <svg class="contact-icon" viewBox="0 0 10 10"><circle cx="5" cy="5" r="5" fill="#1f9ad6"/><path d="M3 2.5l1.2 0 .6 1.5-.8.6a4 4 0 0 0 1.6 1.6l.6-.8 1.5.6v1.2c-3 .3-5-1.8-4.7-4.7z" fill="#fff"/></svg>
        +61 400 123 987
      </div>
      <div class="contact-row">
        <svg class="contact-icon" viewBox="0 0 10 10"><circle cx="5" cy="5" r="5" fill="#1f9ad6"/><rect x="2.3" y="3.2" width="5.4" height="3.6" fill="#fff"/><path d="M2.3 3.2L5 5.3 7.7 3.2" stroke="#1f9ad6" stroke-width=".6" fill="none"/></svg>
        mail@bytemill.co
      </div>
    </address>

    <div class="watermark"></div>

    <section class="letter">
      <div class="date">January 12, 2014</div>
      <div class="recipient">
        Mr. John Doe<br>President<br>AA Corporation<br>111 Street Name, Suite#<br>City, State, 12345
      </div>
      <div class="salutation">Dear Mr. John,</div>
      <p>Lorem Ipsum is simply dummy text of the printing and typesetting industry. Lorem Ipsum has been the industry's standard dummy text ever since the 1500s, when an unknown printer took a galley of type and scrambled it to make a type specimen book. It has survived not only five centuries, but also the leap into electronic typesetting, remaining essentially unchanged.</p>
      <p>The standard chunk of Lorem Ipsum used since the 1500s is reproduced below for those interested. Sections 1.10.32 and 1.10.33 from "de Finibus Bonorum et Malorum" by Cicero are also reproduced in their exact original form, accompanied by English versions from the 1914 translation by H. Rackham</p>
      <p>Lorem Ipsum is simply dummy text of the printing and typesetting industry. Lorem Ipsum has been the industry's standard dummy text ever since the 1500s, when an unknown printer took a galley of type and scrambled it to make a type specimen book. It has survived not only five centuries, but also the leap into electronic typesetting, remaining essentially unchanged. It was popularised in the</p>
      <div class="closing">Sincerely Your,</div>
      <div class="signature" role="img" aria-label="Handwritten signature"></div>
      <div>Name Last Name<br>Company Name</div>
    </section>

    <div class="side-bar"><span>www.bytemill.co</span></div>

    <svg class="footer-bands" viewBox="0 0 537 90" aria-hidden="true">
      <polygon points="0,90 0,82 165,82 175,72 320,72 330,62 470,62 480,52 537,52 537,90" fill="#3b3b3d"/>
      <polygon points="0,80 163,80 170,73 7,73" fill="#1f9ad6"/>
      <polygon points="175,70 318,70 325,63 182,63" fill="#3b3b3d"/>
      <polygon points="330,60 468,60 475,53 337,53" fill="#1f9ad6"/>
    </svg>
  </main>
</body>
</html>
```